Boutique winery needs new wine label

domaine Verlin is a boutique wine company based in the Clare Valley of South Australia. We are an established brand, best known for our Riesling and Grenache. We plan to launch a new sub brand called La Douce ferme and require a new label that is different from the others we use. It will be used on small batch Riesling and should have a rustic but quality feel. Attached is a small image of the house where the winery is based. The label should incorporate a hand drawn sketch of the house.
Target Market(s)
High end wine consumers with an interest in Riesling
Requirements
Must have
- hand drawn sketch of the house
- the name of the wine La Douce ferme present on the front label
- Vintage (2018) and region (Clare Valley) present on the front label
- Minimal use of colour on the label but would look at embellishments such as gold foil
Nice to have
- A clean, simple style of label, preferably with white background
- La Douce ferme written in script style
Should not have
- domaine Verlin written on the front label
- the current domaine Verlin logo

```html
<!DOCTYPE html>
<html lang="en">
<head>
<meta charset="utf-8">
<title>La Douce ferme – Wine Label</title>
<link rel="stylesheet" href="https://fonts.googleapis.com/css2?family=Felipa&family=Alice&display=swap">
<style>
  :root {
    --label-black: #000000;
    --label-white: #ffffff;
    --ink: #111111;
    --gold-deep: #e2b02c;
    --gold-light: #fbef7c;
    --gold-bronze: #ad621a;
    --gold-amber: #ef9c2e;
    --sketch-dark: #4a5250;
    --sketch-light: #c9cfcd;
    --gold-band: linear-gradient(90deg,
      var(--gold-deep) 0%,
      var(--gold-light) 18%,
      var(--gold-bronze) 42%,
      var(--gold-amber) 62%,
      var(--gold-light) 82%,
      var(--gold-deep) 100%);
  }
  * { margin: 0; padding: 0; box-sizing: border-box; }
  html, body {
    width: 1134px;
    height: 1200px;
    overflow: hidden;
    background: var(--label-black);
  }
  .label {
    position: relative;
    width: 1134px;
    height: 1200px;
    background: var(--label-black);
  }
  .label__frame {
    position: absolute;
    left: 138px;
    top: 127px;
    width: 888px;
    height: 928px;
    background: var(--gold-band);
    padding: 14px;
  }
  .label__panel {
    position: relative;
    width: 100%;
    height: 100%;
    background: var(--label-white);
  }
  .label__title {
    position: absolute;
    left: 0;
    right: 0;
    top: 92px;
    text-align: center;
    font-family: "Felipa", cursive;
    font-size: 108px;
    line-height: 1;
    font-weight: 400;
    color: var(--ink);
  }
  .label__house {
    position: absolute;
    left: 163px;
    top: 259px;
    width: 536px;
    height: 336px;
    background: var(--gold-band);
    padding: 5px;
  }
  .label__house-sketch {
    width: 100%;
    height: 100%;
    background:
      linear-gradient(180deg, var(--label-white) 0%, var(--label-white) 12%, var(--sketch-light) 30%, var(--sketch-dark) 100%);
  }
  .label__details {
    position: absolute;
    left: 0;
    right: 0;
    top: 680px;
    text-align: center;
    font-family: "Alice", serif;
    font-size: 50px;
    line-height: 94px;
    letter-spacing: 3px;
    color: var(--ink);
  }
</style>
</head>
<body>
  <main class="label">
    <div class="label__frame">
      <div class="label__panel">
        <h1 class="label__title">La Douce ferme</h1>
        <figure class="label__house">
          <div class="label__house-sketch" role="img" aria-label="Hand-drawn sketch of the two-storey stone winery house with shuttered windows and climbing vines"></div>
        </figure>
        <div class="label__details">
          <p class="label__vintage">Vintage 2018</p>
          <p class="label__region">Clare Valley</p>
        </div>
      </div>
    </div>
  </main>
</body>
</html>
```